I want to thank you very much for all your great designs. It was a really tough choice, but I have finally chosen a winner. I have been very happy with this process and very pleased with all the great choices I was given. I will definitely refer this company to my friends and tell them that they will get exactly what they are looking for from many, very talented designers. Thanks again! Dana
Hello All.
When doing that additional return address label,
Include:
- Logo
- Company Name
- Address
- Design Concept
- Size: 4"X3" (inches) return label
Thanks
Hello Designers! Great work that I'm seeing! If I have starred one of your designs, you should have received private messages regarding them by now. If not, please message me.
Can you please be sure to resubmit those designs with the changes I have requested because if I starred it, I'm considering it as my choice.
Don't forget to review the general comments in case I didn't add those things in your private messages.
One thing I wanted to add to the general comments is the fact that I somehow want "The Builder's Coverage Advisors" to be incorporated large on the back of the cards.
After I get the updated designs and I will re-star them. I would then like to start receiving the stationery layouts from the top designs I pick. Besides the letterhead and #10 return envelope I will also need a design for a return address label/sticker for a large 9X11 envelope.
Thanks for your participation. I look for to the updated designs. Dana
Hi. Thanks so much for all your designs. Just a couple of general comments.
I do like the more colorful cards using the gold as an accent only. I prefer the blue and black and white more for large sections or entire backgrounds.
I would like either spaces or periods between all the phone numbers, please. example: 555.418.3927 or 555 418 3927
License number can simply be License# .......
I haven't decided if I like the symbols next to the phone, fax, email, web yet. Can I see some different options instead of symbols so I can decide.
Thanks again for your time and great work. I look forward to choosing the winning design. Dana
I haven't decided if I like the symbols next to the phone, fax, email, web. Can I see some different options instead of symbols.
Thanks for your time and great work. I look forward to choosing the winning design. Dana
RT/PHW/NC Team
#8 I like this one too. Like the added info on back. Also can you please add the license number so I can see that on there. We have to advertise our insurance license for the company and individuals. Thanks
#2 I like this design. Please add & refer to the information requested on card in the design request area and the comments section for information on what info I want on the back. I'd like to see it with all my data, please. Please also add spacing or characters on the phone numbers. Thanks so much.

```html
<!DOCTYPE html>
<html lang="en">
<head>
<meta charset="utf-8">
<title>Halvorsen Insurance Services — Stationery</title>
<link rel="stylesheet" href="https://fonts.googleapis.com/css2?family=Cinzel:wght@400;600&family=Open+Sans:wght@400;600;700&display=swap">
<style>
  :root{
    --navy:#1d3560;
    --blue:#2e5c8f;
    --blue-light:#5b86b5;
    --gold:#b89c5c;
    --gray:#6a6d72;
    --ink:#3b3e44;
    --paper:#ffffff;
    --stage:#e6e7e9;
    --band:#2b3a6b;
  }
  *{box-sizing:border-box;margin:0;padding:0}
  html,body{width:1200px;height:1011px;overflow:hidden}
  body{position:relative;background:var(--stage);font-family:"Open Sans",Arial,sans-serif;color:var(--ink)}

  .title-band{position:absolute;left:0;top:0;width:1200px;height:70px;background:linear-gradient(90deg,var(--band),#4a5a8e);display:flex;align-items:center;padding-left:40px}
  .title-band h1{font-family:"Cinzel",Georgia,serif;font-weight:400;font-size:30px;color:#fff;letter-spacing:1px}

  .sheet{position:absolute;background:var(--paper);box-shadow:0 4px 14px rgba(0,0,0,.18);overflow:hidden}
  .sheet svg.deco{position:absolute;display:block}

  .brand{display:flex;align-items:center;gap:10px}
  .brand-mark{flex:none;border-radius:50%;background:var(--navy)}
  .brand-name{font-weight:700;color:var(--navy);line-height:1.1}

  /* letterhead */
  .letterhead{left:50px;top:110px;width:600px;height:776px}
  .letterhead .brand{position:absolute;left:44px;top:44px}
  .letterhead .brand-mark{width:46px;height:46px}
  .letterhead .brand-name{font-size:22px;width:170px}
  .letterhead .contact{position:absolute;right:44px;top:50px;font-size:10.5px;line-height:1.6;color:var(--gray);text-align:right}
  .letterhead .deco{left:0;bottom:0;width:600px;height:130px}
  .letterhead .web{position:absolute;left:40px;bottom:12px;font-size:12px;color:#fff;font-weight:600;letter-spacing:.3px}

  /* envelope */
  .envelope{left:690px;top:110px;width:460px;height:200px}
  .envelope .deco{right:0;top:0;width:460px;height:80px}
  .envelope .brand{position:absolute;left:26px;top:40px}
  .envelope .brand-mark{width:34px;height:34px}
  .envelope .brand-name{font-size:16px;width:130px}
  .envelope .return{position:absolute;left:26px;top:100px;font-size:9.5px;color:var(--gray)}

  /* business card front */
  .card{width:340px;height:194px}
  .card-front{left:690px;top:350px}
  .card-front .brand{position:absolute;left:18px;top:50px;flex-direction:column;align-items:flex-start;gap:6px}
  .card-front .brand-mark{width:36px;height:36px}
  .card-front .brand-name{font-size:15px;width:120px}
  .card-front .divider{position:absolute;left:152px;top:40px;width:1px;height:100px;background:#c9ccd1}
  .card-front .person{position:absolute;left:166px;top:34px}
  .card-front .person-name{font-size:15px;font-weight:700;letter-spacing:.5px;text-transform:uppercase}
  .card-front .person-name .first{color:var(--gray)}
  .card-front .person-name .last{color:var(--blue)}
  .card-front .role{font-size:9px;color:var(--gray);margin-bottom:6px}
  .card-front .details{font-size:8.5px;line-height:1.55;color:var(--ink);list-style:none}
  .card-front .details li{display:flex;align-items:center;gap:5px}
  .card-front .details svg{width:8px;height:8px;flex:none}
  .card-front .deco{left:0;bottom:0;width:340px;height:40px}

  /* business card back */
  .card-back{left:690px;top:574px}
  .card-back .deco{left:0;top:0;width:340px;height:194px}
  .card-back .brand{position:absolute;left:16px;top:14px}
  .card-back .brand-mark{width:26px;height:26px}
  .card-back .brand-name{font-size:12px;width:110px}
  .card-back .tagline{position:absolute;left:16px;top:72px;font-size:10.5px;font-weight:700;color:#fff;letter-spacing:.6px;text-transform:uppercase}
  .card-back .services{position:absolute;left:16px;top:92px;list-style:none;font-size:8.5px;line-height:1.6;color:#dfe7f2}
  .card-back .services li::before{content:"";display:inline-block;width:4px;height:4px;background:var(--gold);margin-right:6px;vertical-align:middle}
  .card-back .phone{position:absolute;right:16px;bottom:20px;font-size:11px;font-weight:700;color:#fff;letter-spacing:.4px}
</style>
</head>
<body>

<header class="title-band"><h1>Stationary Design For</h1></header>

<!-- Letterhead -->
<section class="sheet letterhead">
  <div class="brand"><span class="brand-mark"></span><span class="brand-name">Halvorsen Insurance Services</span></div>
  <address class="contact">
    2290 Larkspur Lane #214<br>Ridgeview, CA 90000<br>
    P 555.418.3927<br>F 555.418.3928<br>dana@halvorseninsure.com<br>License# 0X12345
  </address>
  <svg class="deco" viewBox="0 0 600 130" preserveAspectRatio="none" aria-hidden="true">
    <defs><linearGradient id="lhBlue" x1="0" x2="1"><stop offset="0" stop-color="#1d3560"/><stop offset="1" stop-color="#5b86b5"/></linearGradient></defs>
    <path d="M0 60 C180 110 380 20 600 40 L600 130 L0 130 Z" fill="url(#lhBlue)"/>
    <path d="M0 98 C200 120 400 70 600 82 L600 130 L0 130 Z" fill="#b89c5c"/>
    <path d="M0 108 C200 128 400 86 600 96 L600 130 L0 130 Z" fill="#a88a4a"/>
  </svg>
  <span class="web">www.halvorseninsure.com</span>
</section>

<!-- #10 Envelope -->
<section class="sheet envelope">
  <svg class="deco" viewBox="0 0 460 80" preserveAspectRatio="none" aria-hidden="true">
    <defs><linearGradient id="envBlue" x1="0" x2="1"><stop offset="0" stop-color="#5b86b5"/><stop offset="1" stop-color="#1d3560"/></linearGradient></defs>
    <path d="M200 0 C280 40 380 60 460 50 L460 0 Z" fill="url(#envBlue)"/>
    <path d="M230 0 C300 30 390 46 460 40 L460 46 C390 54 300 40 220 0 Z" fill="#b89c5c"/>
  </svg>
  <div class="brand"><span class="brand-mark"></span><span class="brand-name">Halvorsen Insurance Services</span></div>
  <p class="return">2290 Larkspur Lane #214, Ridgeview, CA 90000</p>
</section>

<!-- Business card front -->
<section class="sheet card card-front">
  <div class="brand"><span class="brand-mark"></span><span class="brand-name">Halvorsen Insurance Services</span></div>
  <span class="divider"></span>
  <div class="person">
    <p class="person-name"><span class="first">Dana</span> <span class="last">Halvorsen</span></p>
    <p class="role">President</p>
    <ul class="details">
      <li><svg viewBox="0 0 8 8"><circle cx="4" cy="3" r="2.2" fill="#2e5c8f"/><path d="M4 8 L2 4 H6 Z" fill="#2e5c8f"/></svg>2290 Larkspur Lane #214, Ridgeview, CA 90000</li>
      <li><svg viewBox="0 0 8 8"><rect x="2" y="0" width="4" height="8" rx="1" fill="#2e5c8f"/></svg>555.418.3927</li>
      <li><svg viewBox="0 0 8 8"><rect x="0" y="2" width="8" height="5" fill="#2e5c8f"/></svg>555.418.3928</li>
      <li><svg viewBox="0 0 8 8"><rect x="0" y="1" width="8" height="6" fill="none" stroke="#2e5c8f"/><path d="M0 1 L4 4 L8 1" fill="none" stroke="#2e5c8f"/></svg>dana@halvorseninsure.com</li>
      <li><svg viewBox="0 0 8 8"><circle cx="4" cy="4" r="3.5" fill="#b89c5c"/></svg>License# 0X12345</li>
    </ul>
  </div>
  <svg class="deco" viewBox="0 0 340 40" preserveAspectRatio="none" aria-hidden="true">
    <path d="M0 28 C120 10 230 30 340 12 L340 40 L0 40 Z" fill="#2e5c8f"/>
    <path d="M0 34 C120 20 230 36 340 22 L340 26 C230 40 120 24 0 38 Z" fill="#b89c5c"/>
  </svg>
</section>

<!-- Business card back -->
<section class="sheet card card-back">
  <svg class="deco" viewBox="0 0 340 194" preserveAspectRatio="none" aria-hidden="true">
    <defs><linearGradient id="backBlue" x1="0" y1="0" x2="1" y2="1"><stop offset="0" stop-color="#1d3560"/><stop offset="1" stop-color="#3f6fa3"/></linearGradient></defs>
    <path d="M0 56 C110 70 230 40 340 54 L340 194 L0 194 Z" fill="url(#backBlue)"/>
    <path d="M0 52 C110 66 230 36 340 50 L340 54 C230 40 110 70 0 56 Z" fill="#b89c5c"/>
    <rect x="0" y="186" width="340" height="8" fill="#b89c5c"/>
  </svg>
  <div class="brand"><span class="brand-mark"></span><span class="brand-name">Halvorsen Insurance Services</span></div>
  <p class="tagline">The Builder's Coverage Advisors</p>
  <ul class="services">
    <li>General Liability</li>
    <li>Workers Compensation</li>
    <li>Commercial Auto</li>
    <li>Surety Bonds</li>
    <li>Builders Risk</li>
  </ul>
  <p class="phone">555.418.3927</p>
</section>

</body>
</html>
```